5868 7090

Web(re)design of an existing directory search site www.le7090x.be (in Dutch www.de5868x.be and in English www.3969x.be).

This site is a directory site, i.e. a "white pages" site whereby people can search the phone & details of another person based on a combination of name + city (for instance darrow in Brussels); one can also search a company also based on a combination of name + city (for instance Vornex in Brussels); last but not least one can also search the name of the subscriber behind a specific telephone number (also called reverse search).

This site is quite outdated and needs a redesign, see instructions.

We need the output in XD format.

```html
<!DOCTYPE html>
<html lang="fr">
<head>
<meta charset="utf-8">
<title>70-90 – Renseignements</title>
<link href="https://fonts.googleapis.com/css2?family=Roboto+Condensed:wght@400;700&family=Roboto:wght@400&display=swap" rel="stylesheet">
<style>
  :root{
    --red:#d0121b;
    --red-dark:#b80f17;
    --nav-bg:rgba(12,10,9,.92);
    --white:#ffffff;
    --ink:#1a1a1a;
    --panel:rgba(10,8,7,.82);
    --hint:#e6e0da;
  }
  *{box-sizing:border-box;margin:0;padding:0}
  html,body{width:1200px;height:600px;overflow:hidden;background:var(--white)}
  body{font-family:"Roboto Condensed",Arial,sans-serif;position:relative;color:var(--ink)}

  .hero{position:absolute;left:0;top:0;width:1200px;height:514px;
    background:
      radial-gradient(ellipse 260px 300px at 560px 260px, #8a4a30 0%, rgba(90,45,28,.6) 45%, transparent 75%),
      radial-gradient(ellipse 260px 220px at 880px 180px, #a8742e 0%, rgba(120,80,30,.5) 50%, transparent 80%),
      radial-gradient(ellipse 200px 200px at 220px 300px, #4a3a30 0%, transparent 80%),
      linear-gradient(180deg,#2a211c 0%,#3b2a22 50%,#2b201b 100%);}

  .topbar{position:absolute;left:0;top:0;width:1200px;height:64px;background:var(--nav-bg)}
  .nav{position:absolute;top:0;left:0;height:64px;width:1200px;font-size:19px;color:var(--white)}
  .nav a{position:absolute;top:0;height:64px;line-height:66px;color:var(--white);text-decoration:none}
  .nav .active{background:var(--red);left:513px;width:126px;text-align:center}
  .lang{position:absolute;left:1098px;top:0;line-height:64px;font-size:18px;color:var(--white)}
  .lang small{font-size:10px;margin-left:4px}
  .burger{position:absolute;left:1155px;top:25px;width:23px}
  .burger span{display:block;height:2px;background:var(--white);margin-bottom:5px}

  .brand-disc{position:absolute;left:-137px;top:-187px;width:354px;height:354px;border-radius:50%;background:var(--white)}
  .brand{position:absolute;left:30px;top:48px;display:flex;align-items:center;gap:8px;font-weight:700;font-size:40px;color:var(--red)}
  .brand i{width:18px;height:18px;border-radius:50%;background:var(--red);display:block}

  .watermark{position:absolute;left:930px;top:205px;font-weight:700;font-size:96px;color:rgba(255,255,255,.22);letter-spacing:2px}

  .title{position:absolute;left:172px;top:254px;font-size:38px;font-weight:700;color:var(--white);text-shadow:0 2px 4px rgba(0,0,0,.5)}

  .search{position:absolute;left:172px;top:320px;width:717px;height:79px;background:var(--panel)}
  .field{position:absolute;top:12px;width:191px}
  .field .box{height:32px;background:var(--white);font-weight:700;font-size:14px;line-height:32px;padding-left:9px;color:var(--ink)}
  .field .hint{margin-top:9px;font-size:12px;color:var(--hint)}
  .go{position:absolute;left:617px;top:12px;width:91px;height:32px;background:var(--red);color:var(--white);font-weight:700;font-size:14px;display:flex;align-items:center;justify-content:center;gap:9px}

  .check{position:absolute;left:172px;top:409px;width:224px;height:54px;background:#f9f9f9;border:1px solid #d3d3d3;font-family:Roboto,Arial,sans-serif}
  .check .tick{position:absolute;left:9px;top:16px;width:20px;height:20px;border:2px solid #c1c1c1;border-radius:2px;background:var(--white)}
  .check .lbl{position:absolute;left:38px;top:19px;font-size:11px;color:#222}
  .check .mark{position:absolute;right:8px;top:6px;text-align:center;font-size:7px;color:#555}
  .check .mark b{display:block;width:22px;height:22px;margin:0 auto 3px;border-radius:50%;background:#4a90e2}

  .footer{position:absolute;left:0;top:514px;width:1200px;height:86px}
  .links{position:absolute;left:172px;top:22px;font-size:14px;color:var(--ink)}
  .links span{margin:0 8px}
  .copy{position:absolute;left:172px;top:43px;font-size:14px}
  .badge{position:absolute;left:937px;top:18px;width:62px;height:62px;border-radius:50%;background:#e9e9e9}
</style>
</head>
<body>
  <div class="hero" role="img" aria-label="Photo d'ambiance : une personne dans un café tenant une boisson et consultant son téléphone"></div>

  <header class="topbar">
    <nav class="nav">
      <a class="active" href="#">Particuliers</a>
      <a href="#" style="left:662px">Sociétés</a>
      <a href="#" style="left:770px">Annuaire inversé</a>
      <a href="#" style="left:935px">International</a>
    </nav>
    <div class="lang">FR<small>&#8964;</small></div>
    <div class="burger"><span></span><span></span><span></span></div>
  </header>

  <div class="brand-disc"></div>
  <div class="brand"><i></i>70·90</div>

  <div class="watermark">70·90</div>

  <h1 class="title">Les Renseignements SEPTANTE-NONANTE Utiles</h1>

  <form class="search">
    <div class="field" style="left:12px"><div class="box">Nom de famille:</div><div class="hint">Ex: Dupont, Janssens, ...</div></div>
    <div class="field" style="left:214px"><div class="box">Prénom:</div><div class="hint">Ex: Jan, Louis, ...</div></div>
    <div class="field" style="left:416px"><div class="box">Localité:</div><div class="hint">Ex: Liége, Anvers, 1150, ....</div></div>
    <div class="go">
      <svg width="18" height="18" viewBox="0 0 18 18" fill="none" stroke="#fff" stroke-width="1.6"><circle cx="7.5" cy="7.5" r="6"/><line x1="12" y1="12" x2="17" y2="17"/></svg>
      70-90!
    </div>
  </form>

  <div class="check">
    <div class="tick"></div>
    <div class="lbl">I'm not a robot</div>
    <div class="mark"><b></b>SafeCheck<br>Privacy · Terms</div>
  </div>

  <footer class="footer">
    <div class="links">B2B Services<span>|</span>Aide<span>|</span>Conditions générales d'utilisation<span>|</span>Respect de la vie privée</div>
    <div class="copy">Copyright Norvane 2022, tous droits réservés.</div>
    <div class="badge" aria-hidden="true"></div>
  </footer>
</body>
</html>
```